Motorcycle Shop Business Card

New business card for Motorcycle repair and customization shop.Business name: Copper Falcon Chris Morris443-865-5190, 7214 Quarry Lane Linden Vale, MD 21990. www.dale@copperfalconcustoms.example. I uploaded some motorcycle images and logo and a couple of our calendar shoots. They do not have to be used on card just examples of some of our work and past graphic work.
We work on Vantor Brennick and Custom Built Motorcycles.

Looking for front and back design

Target Market(s)

Motorcycle owners

Industry/Entity Type

Motorcycle Part

```html
<!DOCTYPE html>
<html lang="en">
<head>
<meta charset="UTF-8">
<title>Copper Falcon Customs – Business Card</title>
<link href="https://fonts.googleapis.com/css2?family=Fira+Sans:wght@500;600&display=swap" rel="stylesheet">
<style>
  :root {
    --backdrop: #1d1d1d;
    --card-light: #ffffff;
    --card-dark: #2c2c2c;
    --ink-dark: #231f20;
    --ink-light: #ffffff;
    --rule: #231f20;
  }
  * { margin: 0; padding: 0; box-sizing: border-box; }
  html, body {
    width: 1200px;
    height: 897px;
    overflow: hidden;
    background: var(--backdrop);
    font-family: "Fira Sans", sans-serif;
    font-feature-settings: "onum" 1;
  }
  .canvas { position: relative; width: 1200px; height: 897px; }

  .card { position: absolute; left: 303px; width: 594px; height: 340px; }
  .card--front { top: 92px; background: var(--card-light); }
  .card--back { top: 470px; height: 338px; background: var(--card-dark); }

  .contact-block { position: absolute; left: 39px; top: 56px; color: var(--ink-dark); }
  .contact-block__name { font-size: 36px; font-weight: 600; line-height: 1; margin-bottom: 16px; }
  .contact-block__address { font-size: 22px; font-weight: 600; line-height: 31px; }

  .divider { position: absolute; left: 301px; top: 56px; width: 2px; height: 120px; background: var(--rule); }

  .brand-name {
    position: absolute;
    font-weight: 600;
    text-align: center;
    line-height: 1.05;
  }
  .card--front .brand-name { left: 318px; width: 260px; top: 82px; font-size: 32px; color: var(--ink-dark); }
  .card--back .brand-name { left: 0; width: 100%; top: 122px; font-size: 46px; color: var(--ink-light); }

  .contact-band {
    position: absolute; left: 0; bottom: 0; width: 100%; height: 104px;
    background: var(--card-dark); color: var(--ink-light);
    display: flex; flex-direction: column; align-items: center; justify-content: center;
    font-size: 21px; font-weight: 600; line-height: 31px;
  }
</style>
</head>
<body>
<main class="canvas">
  <section class="card card--front">
    <div class="contact-block">
      <p class="contact-block__name">Dale Fenwick</p>
      <p class="contact-block__address">7214 Quarry Lane<br>Linden Vale, MD 21990</p>
    </div>
    <div class="divider"></div>
    <p class="brand-name">Copper Falcon<br>Customs</p>
    <div class="contact-band">
      <p>Phone: 410-555-0137</p>
      <p>www.dale@copperfalconcustoms.example</p>
    </div>
  </section>

  <section class="card card--back">
    <p class="brand-name">Copper Falcon<br>Customs</p>
  </section>
</main>
</body>
</html>
```